Flyer PRTW

Everyone deserves true happiness.
Real Food is the answer to:
A body you love
Reverting illnesses
Healthy digestion
Stable blood sugar
Emotions in control
Blasting energy
Sound sleep
REAL food + water + exercise + Laughter =
“HIGH QUALITY OF LIFE “
EASY, right?
Challenging: certainly
Changing habits: reluctance in sight!
WE’RE OFFER TO:
1. Study YOUR unique body composition, food cravings, blockages, illnesses, and personality!
2. Introduce you to new Food
3. customized wellness plan with follow ups
4. meditation,cooking, and fitness classes as well as wellness workshops
5. New friends with high aspirations
LOGO
Contact info
Please visit our web address to see our design style and colors: www.pinerivertallwave.net
Target Market(s)
people who want to be more healthy
Industry/Entity Type
Fitness
Requirements
Must have
- beautiful pictures of fresh food (main picture) and maybe a few more small pictures reflecting
exercise
healthy living
meditation
Nice to have
- look is crucial. recall some of the color or colors from my logo to have a theme

```html
<!DOCTYPE html>
<html lang="en">
<head>
<meta charset="utf-8">
<title>PRTW Flyer</title>
<link rel="stylesheet" href="https://fonts.googleapis.com/css2?family=Arimo:wght@400;700&family=Short+Stack&display=swap">
<style>
:root{
  --green:#8cc63f;
  --green-dark:#4aa63b;
  --green-pale:#cfe7a8;
  --orange:#f7941d;
  --orange-light:#f9ad4d;
  --peach:#fbd1a6;
  --teal:#1aa07a;
  --ring:#2aa89a;
  --blue:#2ba8d8;
  --red:#ee4423;
  --ink:#3b2a20;
  --white:#ffffff;
  --grey:#8c8c8c;
}
*{margin:0;padding:0;box-sizing:border-box}
html,body{width:1200px;height:848px;overflow:hidden;background:#fff}
body{font-family:"Arimo",Arial,sans-serif}
.flyer{position:relative;width:1200px;height:848px;overflow:hidden}
.panel{position:absolute;top:0;height:848px;overflow:hidden}
.panel--left{left:0;width:399px;background:var(--green)}
.panel--middle{left:399px;width:399px;background:var(--white)}
.panel--right{left:798px;width:402px;background:var(--orange)}
.circle{position:absolute;border-radius:50%;display:flex;flex-direction:column;align-items:center;justify-content:center;text-align:center;white-space:nowrap}
.photo{position:absolute;border-radius:50%;border:6px solid var(--white)}
.hand{font-family:"Short Stack",cursive;line-height:1.1}
.pattern{position:absolute;left:0;top:0}

/* left */
.photo--food{left:-40px;top:-24px;width:394px;height:394px;border-width:9px;background:radial-gradient(circle at 40% 60%,#7ba33a,#c9382a 45%,#e9c24a 75%,#6a8c2c)}
.photo--meditation{left:285px;top:0;width:128px;height:128px;background:radial-gradient(circle,#f1efe8,#c8c3b4)}
.headline{position:absolute;color:var(--white);font-weight:700;line-height:1;white-space:nowrap}
.headline--everyone{left:64px;top:42px;font-size:40px}
.headline--deserves{left:28px;top:76px;font-size:60px}
.headline--true{left:242px;top:122px;font-size:36px}
.headline--happiness{left:70px;top:146px;font-size:34px}
.answer{left:140px;top:183px;width:176px;height:176px;background:var(--white);font-weight:700;line-height:.92}
.answer .a-real{color:var(--green);font-size:32px}
.answer .a-food{color:var(--green);font-size:30px}
.answer .a-the{color:var(--orange);font-size:20px;align-self:flex-end;margin-right:30px}
.answer .a-answer{color:var(--orange);font-size:36px}
.answer .a-to{color:var(--orange);font-size:30px}
.photo--class{left:245px;top:342px;width:142px;height:142px;background:radial-gradient(circle,#b9d29a,#5e8a3e)}
.benefit--body{left:4px;top:330px;width:196px;height:196px;background:var(--orange-light);color:var(--ink);font-size:25px}
.benefit--sugar{left:134px;top:440px;width:174px;height:174px;background:var(--white);color:var(--blue);font-size:22px;border:4px solid var(--green-pale)}
.benefit--illness{left:14px;top:491px;width:100px;height:100px;background:var(--green-pale);color:var(--ink);font-size:14px;border:4px solid var(--white)}
.benefit--sleep{left:290px;top:567px;width:112px;height:112px;background:var(--orange);color:var(--white);font-size:23px;border:6px solid var(--white)}
.benefit--digestion{left:-8px;top:606px;width:128px;height:128px;background:var(--orange-light);color:var(--blue);font-size:19px}
.photo--portrait{left:110px;top:615px;width:194px;height:194px;background:radial-gradient(circle,#e8dccf,#a7b7c4)}
.benefit--energy{left:14px;top:734px;width:128px;height:128px;background:var(--green-dark);color:var(--white);font-size:20px}
.benefit--emotions{left:261px;top:727px;width:142px;height:142px;background:var(--blue);color:var(--green);font-size:18px}

/* middle */
.logo-ring{position:absolute;left:44px;top:-114px;width:314px;height:314px;border-radius:50%;border:7px solid var(--ring)}
.brand{position:absolute;left:60px;top:38px;width:280px;display:flex;align-items:center;justify-content:center;gap:8px}
.brand-dot{width:30px;height:30px;border-radius:50%;background:var(--green)}
.brand-name{font-size:22px;font-weight:700;color:var(--green-dark)}
.brand-tag{position:absolute;left:60px;top:74px;width:280px;text-align:center;font-size:7px;color:var(--green-dark);letter-spacing:.5px}
.site{position:absolute;left:60px;top:98px;width:280px;text-align:center;font-size:14px;color:#222}
.tile{position:absolute;width:107px;height:107px;border-radius:14px;display:flex;align-items:center;justify-content:center;font-weight:700}
.tile svg{width:62px;height:62px}
.t1{left:28px;top:185px;background:var(--green);color:#222;font-size:26px}
.t2{left:150px;top:185px;background:var(--orange-light);color:var(--white);font-size:24px;font-weight:400}
.t3{left:271px;top:185px;background:var(--teal)}
.t4{left:28px;top:306px;background:var(--orange-light);color:var(--blue);font-size:24px}
.t5{left:150px;top:306px;background:var(--orange)}
.t6{left:271px;top:306px;background:var(--green-pale);color:#333;font-size:20px}
.t7{left:28px;top:427px;background:var(--peach)}
.t8{left:150px;top:427px;background:var(--green);color:#222;font-size:26px}
.t9{left:271px;top:427px;background:var(--orange)}
.quality{position:absolute;left:0;top:560px;width:399px;text-align:center;color:var(--red);font-size:27px;font-weight:700}
.photo--group{position:absolute;left:21px;top:605px;width:363px;height:243px;background:linear-gradient(180deg,#ffffff,#d9d4cf 40%,#8a8c92)}

/* right */
.challenge{position:absolute;left:0;top:24px;width:210px;text-align:center;color:var(--white);font-size:19px;line-height:1.2}
.photo--jump{left:240px;top:-26px;width:190px;height:190px;background:linear-gradient(180deg,#2a3b6a,#e89b3b 70%,#3a2a1a)}
.here-ring{position:absolute;left:18px;top:171px;width:428px;height:428px;border-radius:50%;border:6px solid var(--white)}
.here-title{position:absolute;left:0;top:0;color:var(--white);font-weight:700;line-height:1;letter-spacing:-2px;white-space:nowrap}
.here-title .l1{position:absolute;left:135px;top:180px;font-size:58px}
.here-title .l2{position:absolute;left:74px;top:218px;font-size:80px}
.here-title .l2 small{font-size:62px}
.steps{list-style:none;color:var(--white);font-size:16px;line-height:1.2}
.step{position:absolute;display:flex;align-items:center;gap:12px}
.num{flex:none;width:38px;height:38px;border-radius:50%;background:var(--white);color:var(--orange);font-weight:700;font-size:21px;display:flex;align-items:center;justify-content:center}
.step p{text-align:center}
.s1{left:28px;top:312px}.s1 p{width:310px}
.s2{left:24px;top:370px}.s2 p{width:300px}
.s3{left:39px;top:424px}.s3 p{width:260px}
.s4{left:64px;top:472px}.s4 p{width:250px}
.s5{left:119px;top:538px}.s5 p{width:200px}
.photo--pantry{left:0;top:570px;width:156px;height:156px;background:radial-gradient(circle,#f4eee2,#c99a5a 60%,#7a4a2a)}
.contact-blob{position:absolute;left:140px;top:708px;width:380px;height:380px;border-radius:50%;background:var(--green)}
.new-you{position:absolute;left:0;top:0;color:var(--white);line-height:1;white-space:nowrap}
.new-you .y1{position:absolute;left:228px;top:608px;font-size:32px}
.new-you .y2{position:absolute;left:212px;top:630px;font-size:54px;font-weight:700}
.new-you .y3{position:absolute;left:287px;top:681px;font-size:22px}
.contact{position:absolute;left:155px;top:752px;width:240px;text-align:center;color:#1d2a10;white-space:nowrap}
.contact .c1{font-size:15px}
.contact .c2{font-size:28px;margin-top:6px}
.contact .c3{font-size:14px;margin-top:4px}
</style>
</head>
<body>
<main class="flyer">

  <section class="panel panel--left">
    <svg class="pattern" width="399" height="848" viewBox="0 0 399 848" aria-hidden="true">
      <g fill="none" stroke="#a9d46a" stroke-width="3">
        <circle cx="360" cy="270" r="60"/>
        <circle cx="40" cy="420" r="70"/>
        <circle cx="370" cy="520" r="45"/>
        <circle cx="220" cy="830" r="60"/>
      </g>
    </svg>
    <div class="photo photo--food" role="img" aria-label="Fresh fruit and vegetables: tomatoes, grapes, strawberries and greens"></div>
    <div class="photo photo--meditation" role="img" aria-label="Person meditating in a calm white room"></div>
    <div class="headline headline--everyone">Everyone</div>
    <div class="headline headline--deserves">deserves</div>
    <div class="headline headline--true">true</div>
    <div class="headline headline--happiness">happiness</div>
    <div class="circle answer">
      <span class="a-real">Real</span>
      <span class="a-food">Food is</span>
      <span class="a-the">the</span>
      <span class="a-answer">answer</span>
      <span class="a-to">to:</span>
    </div>
    <div class="circle hand benefit--body">A body<br>you love</div>
    <div class="photo photo--class" role="img" aria-label="Outdoor group exercise class in a park"></div>
    <div class="circle hand benefit--sugar">Stable<br>blood sugar</div>
    <div class="circle hand benefit--illness">Reverting<br>illnesses</div>
    <div class="circle hand benefit--sleep">sound<br>sleep</div>
    <div class="circle hand benefit--digestion">Healthy<br>digestion</div>
    <div class="photo photo--portrait" role="img" aria-label="Smiling woman at a fitness class"></div>
    <div class="circle hand benefit--energy">Blasting<br>energy</div>
    <div class="circle hand benefit--emotions">Emotions<br>in control</div>
  </section>

  <section class="panel panel--middle">
    <div class="logo-ring"></div>
    <div class="brand"><span class="brand-dot"></span><span class="brand-name">Pinerivertallwave</span></div>
    <div class="brand-tag">BALANCED NUTRITION, MIND, AND FITNESS</div>
    <div class="site">www.pinerivertallwave.net</div>

    <div class="tile t1">REAL</div>
    <div class="tile t2">food</div>
    <div class="tile t3"><svg viewBox="0 0 60 60" aria-hidden="true"><path d="M22 4h16v18h18v16H38v18H22V38H4V22h18z" fill="#f7941d"/></svg></div>
    <div class="tile t4">water</div>
    <div class="tile t5"><svg viewBox="0 0 60 60" aria-hidden="true"><path d="M22 4h16v18h18v16H38v18H22V38H4V22h18z" fill="#4aa63b"/></svg></div>
    <div class="tile t6">exercise</div>
    <div class="tile t7"><svg viewBox="0 0 60 60" aria-hidden="true"><path d="M22 4h16v18h18v16H38v18H22V38H4V22h18z" fill="#8c8c8c"/></svg></div>
    <div class="tile t8">L.O.L.</div>
    <div class="tile t9"><svg viewBox="0 0 60 60" aria-hidden="true"><rect x="6" y="14" width="48" height="12" fill="#fff"/><rect x="6" y="34" width="48" height="12" fill="#fff"/></svg></div>

    <h2 class="quality">“HIGH QUALITY OF LIFE “</h2>
    <div class="photo--group" role="img" aria-label="Large smiling group of people of all ages"></div>
  </section>

  <section class="panel panel--right">
    <p class="challenge">EASY, right?<br>Challenging: certainly<br>Changing habits:<br>reluctance in sight!</p>
    <div class="photo photo--jump" role="img" aria-label="Friends jumping at sunset by the sea"></div>
    <div class="here-ring"></div>
    <h2 class="here-title"><span class="l1">WE’RE</span><span class="l2">HERE<small>TO:</small></span></h2>
    <ol class="steps">
      <li class="step s1"><span class="num">1</span><p>Study YOUR unique body composition, food cravings, blockages, illnesses, and personality!</p></li>
      <li class="step s2"><span class="num">2</span><p>Introduce you to new Food</p></li>
      <li class="step s3"><span class="num">3</span><p>customized wellness plan with follow ups</p></li>
      <li class="step s4"><span class="num">4</span><p>meditation, cooking, and fitness classes as well as wellness workshops</p></li>
      <li class="step s5"><span class="num">5</span><p>New friends with high aspirations</p></li>
    </ol>
    <div class="photo photo--pantry" role="img" aria-label="Healthy pantry foods: grains in jars, milk, eggs and vegetables"></div>
    <div class="contact-blob"></div>
    <div class="new-you"><span class="y1">a new</span><span class="y2">You</span><span class="y3">is waiting</span></div>
    <div class="contact">
      <p class="c1">You can contact me direct</p>
      <p class="c2">@ 555-014-2273</p>
      <p class="c3">www.pinerivertallwave.net</p>
    </div>
  </section>

</main>
</body>
</html>
```